Heron Freightlines needs Bussiness cards!

Our new trucking company needs business cards!
We need the same design with two different names and emails, everything else it's the same.
I have included our original logo so we can use it for the design.
Note: the logo to be used is the o e with the buffalo on the right side, next to the letters H and F.

Target Market(s)

Trucking, refrigerated transportation, freight

Industry/Entity Type

Business

Contact Information for Business Card

Card #1:
Marcus Tellwright
marcustellwright@heronfreightlines.example
1-844-555-0193
(956)555-0178
3817 W. Tarrow Ave.
Pharr, TX 78599
www.heronfreightlines.example

Card#2:
Orla Brennick
orla@heronfreightlines.example
1-844-555-0193
(956)555-0178
3817 W. Tarrow Ave.
Pharr, TX 78599
www.heronfreightlines.example

Font styles to use
Sans Serif

Colors
0655a3
ec1f27
ffffff

Requirements
Must have
• our logo
Nice to have
• roads on background,

```html
<!DOCTYPE html>
<html lang="en">
<head>
<meta charset="utf-8">
<title>Heron Freightlines business cards</title>
<link rel="stylesheet" href="https://fonts.googleapis.com/css2?family=Arimo:wght@400;700&display=swap">
<style>
  :root {
    --backdrop: #2a2a2a;
    --card: #ffffff;
    --navy: #1b2d57;
    --red: #b7232b;
    --ink: #1e1e1e;
    --rule: #3a3a3a;
  }
  * { box-sizing: border-box; margin: 0; padding: 0; }
  html, body {
    width: 1200px; height: 900px; overflow: hidden;
    background: var(--backdrop);
    font-family: "Arimo", Arial, sans-serif;
  }
  .canvas { position: relative; width: 1200px; height: 900px; }
  .card {
    position: absolute; width: 520px; height: 303px;
    background: var(--card); overflow: hidden;
  }
  .card--front-a { left: 64px; top: 127px; }
  .card--front-b { left: 620px; top: 129px; }
  .card--back-a { left: 64px; top: 492px; }
  .card--back-b { left: 620px; top: 492px; }

  .wordmark {
    position: absolute; display: flex; align-items: center; gap: 8px;
    color: var(--navy); font-weight: 700; line-height: 1; white-space: nowrap;
  }
  .wordmark__dot { width: 12px; height: 12px; border-radius: 50%; background: var(--navy); flex: none; }
  .card__front .wordmark { left: 40px; top: 144px; font-size: 20px; }
  .card__back .wordmark { left: 0; right: 0; top: 140px; justify-content: center; font-size: 34px; }
  .card__back .wordmark__dot { width: 14px; height: 14px; }

  .divider { position: absolute; left: 262px; top: 80px; width: 1px; height: 136px; background: var(--rule); }
  .details {
    position: absolute; left: 280px; top: 90px; right: 10px;
    color: var(--ink); font-size: 10.5px; line-height: 14px; white-space: nowrap;
  }
  .details__name { font-size: 14px; margin-bottom: 11px; }
  .details__address { margin-bottom: 7px; }
  .details__row { display: flex; align-items: center; gap: 5px; line-height: 15px; }
  .details__icon {
    width: 9px; height: 9px; background: var(--red); border-radius: 1px; flex: none;
    color: #fff; font-size: 6px; font-weight: 700; display: flex; align-items: center; justify-content: center;
  }

  .stripe { position: absolute; left: 0; bottom: 0; width: 520px; height: 17px; }

  .web-band {
    position: absolute; left: 0; right: 0; top: 270px; height: 18px;
    background: var(--navy); color: #fff; font-size: 12px; font-weight: 700;
    display: flex; align-items: center; justify-content: center;
  }
</style>
</head>
<body>
<main class="canvas">

  <section class="card card--front-a card__front">
    <div class="wordmark"><span class="wordmark__dot"></span>Heron Freightlines</div>
    <div class="divider"></div>
    <div class="details">
      <p class="details__name">Marcus Tellwright</p>
      <p class="details__address">3817 W. Tarrow Ave.<br>Pharr, TX 78599</p>
      <p class="details__row"><span class="details__icon">P</span>1-844-555-0193</p>
      <p class="details__row"><span class="details__icon">M</span>(956)555-0178</p>
      <p class="details__row"><span class="details__icon">E</span>marcustellwright@heronfreightlines.example</p>
      <p class="details__row"><span class="details__icon">W</span>www.heronfreightlines.example</p>
    </div>
    <svg class="stripe" viewBox="0 0 520 17" aria-hidden="true">
      <polygon points="0,3 248,3 262,17 0,17" fill="var(--red)"/>
      <polygon points="256,3 520,3 520,17 270,17" fill="var(--navy)"/>
      <polygon points="248,3 256,3 270,17 262,17" fill="#fff"/>
    </svg>
  </section>

  <section class="card card--front-b card__front">
    <div class="wordmark"><span class="wordmark__dot"></span>Heron Freightlines</div>
    <div class="divider"></div>
    <div class="details">
      <p class="details__name">Orla Brennick</p>
      <p class="details__address">3817 W. Tarrow Ave.<br>Pharr, TX 78599</p>
      <p class="details__row"><span class="details__icon">P</span>1-844-555-0193</p>
      <p class="details__row"><span class="details__icon">M</span>(956)555-0178</p>
      <p class="details__row"><span class="details__icon">E</span>orla@heronfreightlines.example</p>
      <p class="details__row"><span class="details__icon">W</span>www.heronfreightlines.example</p>
    </div>
    <svg class="stripe" viewBox="0 0 520 17" aria-hidden="true">
      <polygon points="0,3 248,3 262,17 0,17" fill="var(--red)"/>
      <polygon points="256,3 520,3 520,17 270,17" fill="var(--navy)"/>
      <polygon points="248,3 256,3 270,17 262,17" fill="#fff"/>
    </svg>
  </section>

  <section class="card card--back-a card__back">
    <div class="wordmark"><span class="wordmark__dot"></span>Heron Freightlines</div>
    <div class="web-band">www.heronfreightlines.example</div>
  </section>

  <section class="card card--back-b card__back">
    <div class="wordmark"><span class="wordmark__dot"></span>Heron Freightlines</div>
    <div class="web-band">www.heronfreightlines.example</div>
  </section>

</main>
</body>
</html>
```